Meadowlark Suds Business Card

The new business card design will incorporate my new logo components designed by one of your designers. Meadowlark Suds creates high quality soaps and bath products. They would be suited for a Spa, Bed and Breakfast, Boutique environment. The look should be a white background.
Classy, soft and using the colour palet of the logo. The card will be two sided.
Updates

Target Market(s)

Looking to appeal to an upper end market. Spas, boutiques, independent gift stores, bridal salons, bed and breakfast, etc. I want the card to impart a sense of elegance, tranquility and Meadowlark. But also quality and value.

Industry/Entity Type

Business

Font styles to use
Sans Serif
Script

Requirements
Must have
• My logo on the front. But also on the back but faded out to allow written notes on the back.
On the front : Carla Penwick
Owner/Creator
47 Ashgrove Rd
Guelph, Ont K4R 2P9
613.402.9186
Creating Quality Handcrafted Soaps And Bath Products
Custom and Wholesale Orders Welcome
Www.meadowlarksuds-example.ca
Www.facebook.com / MeadowlarkSudsandTub
info@meadowlarksuds-example.ca

```html
<!DOCTYPE html>
<html lang="en">
<head>
<meta charset="utf-8">
<title>Meadowlark Suds Business Card</title>
<link rel="stylesheet" href="https://fonts.googleapis.com/css2?family=Great+Vibes&family=Lato:wght@400;700&display=swap">
<style>
  :root {
    --backdrop: #3b3b3d;
    --card: #ffffff;
    --teal: #9bbdb4;
    --teal-text: #7ea89c;
    --sand: #ead8c8;
    --faint: #e6efec;
  }
  * { box-sizing: border-box; margin: 0; padding: 0; }
  html, body { width: 1200px; height: 901px; overflow: hidden; }
  body { background: var(--backdrop); position: relative; font-family: "Lato", sans-serif; }

  .card {
    position: absolute;
    top: 150px;
    width: 360px;
    height: 600px;
    background: var(--card);
    overflow: hidden;
  }
  .card--back { left: 170px; }
  .card--front { left: 670px; }

  .card__bands { position: absolute; left: 0; bottom: 0; width: 360px; }

  /* back */
  .notes-title {
    position: absolute; top: 40px; left: 0; width: 100%;
    text-align: center; font-family: "Great Vibes", cursive;
    font-size: 68px; color: var(--teal-text); opacity: .85;
  }
  .brand-faded {
    position: absolute; top: 200px; left: 0; width: 100%;
    text-align: center; font-family: "Lato", sans-serif; font-weight: 400;
    font-size: 38px; letter-spacing: 2px; color: var(--faint);
  }
  .tagline {
    position: absolute; top: 352px; left: 30px; width: 300px;
    text-align: center; font-size: 17px; line-height: 1.35;
    color: var(--teal-text); letter-spacing: .3px;
  }

  /* front */
  .brand-name {
    position: absolute; top: 110px; left: 0; width: 100%;
    text-align: center; font-family: "Lato", sans-serif; font-weight: 400;
    font-size: 34px; letter-spacing: 1px; color: var(--teal-text);
  }
  .owner-name {
    position: absolute; top: 205px; left: 0; width: 100%;
    text-align: center; font-family: "Great Vibes", cursive;
    font-size: 46px; color: var(--teal-text);
  }
  .owner-role {
    position: absolute; top: 262px; left: 0; width: 100%;
    text-align: center; font-size: 15px; color: var(--teal-text);
  }
  .address {
    position: absolute; top: 305px; left: 0; width: 100%;
    text-align: center; font-size: 16px; line-height: 1.35; color: var(--teal-text);
  }
  .contact {
    position: absolute; top: 365px; left: 70px; list-style: none;
    font-size: 14px; line-height: 1.55; color: var(--teal-text);
  }
  .contact li { display: flex; align-items: center; gap: 6px; }
  .contact svg { width: 13px; height: 13px; flex: none; }
</style>
</head>
<body>

<section class="card card--back" aria-label="Card back">
  <h2 class="notes-title">Notes:</h2>
  <p class="brand-faded">Meadowlark Suds</p>
  <p class="tagline">Creating Quality Handcrafted Soaps And Bath Products</p>
  <svg class="card__bands" height="260" viewBox="0 0 360 260" aria-hidden="true">
    <path d="M0,20 Q50,190 360,196 L360,206 Q30,206 0,48 Z" fill="var(--sand)"/>
    <path d="M0,78 Q50,222 360,214 L360,260 L0,260 Z" fill="var(--teal)"/>
  </svg>
</section>

<section class="card card--front" aria-label="Card front">
  <p class="brand-name">Meadowlark Suds</p>
  <h1 class="owner-name">Carla Penwick</h1>
  <p class="owner-role">Owner</p>
  <p class="address">47 Ashgrove Rd,<br>Guelph, Ont K4R 2P9</p>
  <ul class="contact">
    <li>
      <svg viewBox="0 0 16 16" aria-hidden="true"><path d="M3 1l3 3-2 2c1 2 3 4 5 5l2-2 3 3-2 3C7 15 1 9 1 3z" fill="var(--teal-text)"/></svg>
      613.402.9186
    </li>
    <li>
      <svg viewBox="0 0 16 16" aria-hidden="true"><circle cx="8" cy="8" r="7" fill="none" stroke="var(--teal-text)" stroke-width="1.5"/><path d="M1 8h14M8 1c-4 4-4 10 0 14M8 1c4 4 4 10 0 14" fill="none" stroke="var(--teal-text)" stroke-width="1.2"/></svg>
      www.meadowlarksuds-example.ca
    </li>
    <li>
      <svg viewBox="0 0 16 16" aria-hidden="true"><circle cx="8" cy="8" r="6" fill="var(--teal-text)"/></svg>
      MeadowlarkSudsandTub
    </li>
  </ul>
  <svg class="card__bands" height="220" viewBox="0 0 360 220" aria-hidden="true">
    <path d="M0,132 Q260,128 356,12 Q280,150 0,150 Z" fill="var(--sand)"/>
    <path d="M0,162 Q260,158 360,22 L360,220 L0,220 Z" fill="var(--teal)"/>
  </svg>
</section>

</body>
</html>
```